Full stationary package for an IT company specialized in personal cloud solutions
Corvanta Integrated Solutions SDN.BHD.
Full stationary package for an IT company specialized in personal cloud solutions - Information Technology
Creative Brief
Simple
Farid Al Mansoor
Managing Director
Jalan Taman Seroja Indah, No.8 Block F, 17B,2C
farid.mansoor@corvanta-example.com
www.corvanta-example.com
2864019 K
FULL STATIONARY PACKAGE DESIGN PLEASE
Only the LOGO

```html
<!DOCTYPE html>
<html lang="en">
<head>
<meta charset="utf-8">
<title>Corvanta Business Cards</title>
<link href="https://fonts.googleapis.com/css2?family=Open+Sans:wght@400;600;700&display=swap" rel="stylesheet">
<style>
  :root {
    --page-bg: #e9e9eb;
    --card-bg: #ffffff;
    --accent-orange: #f7941d;
    --accent-red: #e2411c;
    --brand-blue: #1f5fa8;
    --text-grey: #555a60;
    --rule-grey: #c9ccd1;
  }
  * { margin: 0; padding: 0; box-sizing: border-box; }
  html, body {
    width: 1200px; height: 852px; overflow: hidden;
    background: var(--page-bg);
    font-family: "Open Sans", Arial, sans-serif;
  }
  .canvas { position: relative; width: 1200px; height: 852px; }

  .card {
    position: absolute;
    width: 560px; height: 320px;
    background: var(--card-bg);
    border-radius: 16px;
    overflow: hidden;
    box-shadow: 0 6px 18px rgba(0,0,0,0.18);
  }
  .card--front { left: 30px; top: 110px; }
  .card--back { left: 610px; top: 420px; }

  .card__edge {
    position: absolute; left: 0; top: 0; bottom: 0; width: 16px;
    background: linear-gradient(180deg, var(--accent-orange), var(--accent-red));
  }
  .card__edge::after {
    content: ""; position: absolute; right: -5px; top: 0; bottom: 0; width: 2px;
    background: var(--brand-blue);
  }

  .brand { display: flex; align-items: center; gap: 10px; }
  .brand__dot {
    width: 30px; height: 30px; border-radius: 50%;
    background: var(--accent-orange);
  }
  .brand__name {
    font-weight: 700; font-size: 30px; color: var(--brand-blue);
    letter-spacing: 0.5px;
  }

  .person__name { color: var(--accent-red); font-weight: 600; font-size: 20px; line-height: 1.2; }
  .person__title { color: var(--brand-blue); font-size: 13px; margin-bottom: 8px; }
  .detail { color: var(--text-grey); font-size: 12.5px; line-height: 1.55; }

  .contact { list-style: none; }
  .contact li { display: flex; align-items: center; gap: 7px; color: var(--text-grey); font-size: 12.5px; line-height: 1.75; }
  .contact svg { width: 12px; height: 12px; flex: none; }

  /* front card */
  .card--front .brand { position: absolute; left: 62px; top: 92px; }
  .card--front .person { position: absolute; right: 288px; top: 150px; text-align: right; }
  .card--front .divider {
    position: absolute; left: 290px; top: 140px; width: 1px; height: 110px;
    background: var(--rule-grey);
  }
  .card--front .contact-block { position: absolute; left: 306px; top: 140px; }

  /* back card */
  .card--back .person { position: absolute; left: 240px; top: 40px; }
  .card--back .brand { position: absolute; left: 58px; top: 232px; }
</style>
</head>
<body>
<main class="canvas">

  <section class="card card--front" aria-label="Business card, front">
    <div class="card__edge"></div>
    <div class="brand">
      <span class="brand__dot"></span>
      <span class="brand__name">Corvanta</span>
    </div>
    <div class="person">
      <p class="person__name">Farid Al Mansoor</p>
      <p class="person__title">Managing Director</p>
      <p class="detail">Jalan Taman Seroja Indah</p>
      <p class="detail">No.8, Block F, 17B,2C</p>
    </div>
    <div class="divider"></div>
    <div class="contact-block">
      <p class="detail">Lic No. 2864019 K</p>
      <ul class="contact">
        <li><svg viewBox="0 0 12 12"><circle cx="6" cy="6" r="6" fill="#e2411c"/><path d="M3.5 4.5c.5 1.8 2 3.3 4 4l.9-.9-1.2-.8-.6.5c-.8-.4-1.4-1-1.8-1.8l.5-.6-.8-1.2z" fill="#fff"/></svg>+60-01247780512</li>
        <li><svg viewBox="0 0 12 12"><circle cx="6" cy="6" r="6" fill="#e2411c"/><rect x="3" y="4" width="6" height="4" fill="none" stroke="#fff" stroke-width=".9"/><path d="M3 4l3 2.3L9 4" fill="none" stroke="#fff" stroke-width=".9"/></svg>farid.mansoor@corvanta-example.com</li>
        <li><svg viewBox="0 0 12 12"><circle cx="6" cy="6" r="6" fill="#e2411c"/><circle cx="6" cy="6" r="3" fill="none" stroke="#fff" stroke-width=".9"/><path d="M3 6h6M6 3v6" stroke="#fff" stroke-width=".7"/></svg>www.corvanta-example.com</li>
      </ul>
    </div>
  </section>

  <section class="card card--back" aria-label="Business card, back">
    <div class="card__edge"></div>
    <div class="person">
      <p class="person__name">Farid Al Mansoor</p>
      <p class="person__title">Managing Director</p>
      <p class="detail">Jalan Taman Seroja Indah</p>
      <p class="detail">No.8, Block F, 17B,2C</p>
      <p class="detail" style="margin-top:6px">Lic No. 2864019 K</p>
      <ul class="contact">
        <li><svg viewBox="0 0 12 12"><circle cx="6" cy="6" r="6" fill="#e2411c"/><path d="M3.5 4.5c.5 1.8 2 3.3 4 4l.9-.9-1.2-.8-.6.5c-.8-.4-1.4-1-1.8-1.8l.5-.6-.8-1.2z" fill="#fff"/></svg>+60-01247780512</li>
        <li><svg viewBox="0 0 12 12"><circle cx="6" cy="6" r="6" fill="#e2411c"/><rect x="3" y="4" width="6" height="4" fill="none" stroke="#fff" stroke-width=".9"/><path d="M3 4l3 2.3L9 4" fill="none" stroke="#fff" stroke-width=".9"/></svg>farid.mansoor@corvanta-example.com</li>
        <li><svg viewBox="0 0 12 12"><circle cx="6" cy="6" r="6" fill="#e2411c"/><circle cx="6" cy="6" r="3" fill="none" stroke="#fff" stroke-width=".9"/><path d="M3 6h6M6 3v6" stroke="#fff" stroke-width=".7"/></svg>www.corvanta-example.com</li>
      </ul>
    </div>
    <div class="brand">
      <span class="brand__dot"></span>
      <span class="brand__name">Corvanta</span>
    </div>
  </section>

</main>
</body>
</html>
```